Business card design based on existing website

Please make a business card that is consistent with the look and feel of my new website: http://tellbury.com.sg. By going to the site, I think you'll have all you need in terms of the work I do and the colors I use.

I would like to ask the winner of this project to then do a separate project to design my stationery.

Target Market(s)

Heads of human resources, people wanting psychotherapy, and executives wanting coaching. (It's quite a mix!)

Industry/Entity Type

Psychology

Contact Information for Business Card

Email: ray5678@tellbury.com.sg
Website: http://tellbury.com.sg
Tel: +65 94706218

(I will not have a physical address on the card)

Font styles to use
Serif

Colors

Designer to choose colors to be used in the design.

Requirements
Must have
• On the Front
• ==========
• Have "Dr. Raymond Tellbury" using the font of the website.
• Also "Executive Coach, Psychotherapist, Leadership Professor"
• The back should mention
• ==================
• My degrees
• -------------
• "PhD Kelworth; Post Doc Drayfield". E.g., "Raymond Tellbury (PhD Kelworth; Post Doc Drayfield)" where the text between brackets was in smaller font.
• My work
• ----------
• "Executive coach, psychotherapist, and leadership professor"
• My job titles
• ---------------
• "Principal (Tellbury Consulting)
• Adjunct Professor (Lornvale Commerce University)
• Adjunct Associate Professor (Pemberly Institute of Letters)
• Coach & Supervisor (OKTRAV) '
• Options:
• 1) you can abbreviate Adjunct Professor to "Adj Prof" or "Adj Professor"; and "Adjunct Associate Professor" to "Adj Assoc Prof"
• 2) you abbreviate "Pemberly Institute of Letters" and "Lornvale Commerce University" to "PIL" and "LCU"
• 3) You can also combine the titles for PIL and LCU, e.g., "Adjunct faculty (PIL & LCU)
Nice to have
• Because I work with many Chinese people, it is sometimes helpful to have my family name, "Tellbury", in caps. In the past I have not used caps because it takes away from the aesthetic of the card. Only use caps if it looks good.
• The uploaded image of a "RT" is something that may be helpful. I am undecided.
• THANK YOU for helping me!
Should not have
• No photos. In my industry people consider it overselling.

```html
<!DOCTYPE html>
<html lang="en">
<head>
<meta charset="utf-8">
<title>Dr. Raymond Tellbury – Business Card</title>
<link rel="stylesheet" href="https://fonts.googleapis.com/css2?family=Cardo:wght@400&family=Carlito:wght@400&family=Arimo:wght@400&family=Open+Sans:wght@700&display=swap">
<style>
  :root {
    --page: #ffffff;
    --card-green: #16302a;
    --card-edge: #b9bcb8;
    --mark-tint: #22403a;
    --cream: #ece6cc;
    --band: #a3a28b;
    --band-ink: #1b2a23;
    --back-ink: #e4e6e0;
  }
  * { margin: 0; padding: 0; box-sizing: border-box; }
  html, body {
    width: 1200px; height: 373px; overflow: hidden;
    background: var(--page);
  }
  .canvas { position: relative; width: 1200px; height: 373px; }
  .card {
    position: absolute; top: 31px; width: 542px; height: 304px;
    background: var(--card-green);
    border: 1px solid var(--card-edge);
    overflow: hidden;
  }
  .card--front { left: 25px; }
  .card--back { left: 611px; }

  .mark-placeholder {
    position: absolute; left: 30px; top: 30px;
    width: 120px; height: 120px;
    background: var(--mark-tint);
  }
  .front-name {
    position: absolute; left: 214px; top: 56px;
    font-family: "Cardo", serif; font-weight: 400; font-size: 24px;
    line-height: 30px; color: var(--cream); white-space: nowrap;
  }
  .front-roles {
    position: absolute; left: 222px; width: 240px; top: 100px;
    text-align: center; list-style: none;
    font-family: "Cardo", serif; font-size: 17px; line-height: 21px;
    color: var(--cream);
  }
  .contact-band {
    position: absolute; left: 0; bottom: 0; width: 100%; height: 77px;
    background: var(--band);
  }
  .contact-list {
    position: absolute; left: 207px; width: 270px; top: 8px;
    text-align: center; list-style: none;
    font-family: "Open Sans", sans-serif; font-weight: 700;
    font-size: 11px; line-height: 15.5px; color: var(--band-ink);
    letter-spacing: -0.2px;
  }

  .back-name {
    position: absolute; left: 0; width: 100%; top: 55px; text-align: center;
    font-family: "Carlito", sans-serif; font-weight: 400; font-size: 19px;
    line-height: 22px; color: var(--back-ink);
  }
  .back-degrees {
    position: absolute; left: 0; width: 100%; top: 83px; text-align: center;
    font-family: "Carlito", sans-serif; font-weight: 400; font-size: 12.5px;
    line-height: 15px; color: var(--back-ink);
  }
  .back-titles {
    position: absolute; left: 0; width: 100%; top: 141px; text-align: center;
    list-style: none;
    font-family: "Arimo", sans-serif; font-weight: 400; font-size: 16px;
    line-height: 20.3px; color: var(--back-ink);
  }
</style>
</head>
<body>
<main class="canvas">
  <section class="card card--front" aria-label="Card front">
    <div class="mark-placeholder" role="img" aria-label="Faint monogram mark of Tellbury"></div>
    <h1 class="front-name">Dr. Raymond Tellbury</h1>
    <ul class="front-roles">
      <li>Executive Coach</li>
      <li>Psychotherapist</li>
      <li>Leadership Professor</li>
    </ul>
    <div class="contact-band">
      <ul class="contact-list">
        <li>Tel: +65 94706218</li>
        <li>Email: ray5678@tellbury.com.sg</li>
        <li>Website: http://tellbury.com.sg</li>
      </ul>
    </div>
  </section>

  <section class="card card--back" aria-label="Card back">
    <h2 class="back-name">Raymond Tellbury</h2>
    <p class="back-degrees">(PhD Kelworth; Post Doc Drayfield)</p>
    <ul class="back-titles">
      <li>Principal (Tellbury Consulting)</li>
      <li>Adj. Professor (LCU)</li>
      <li>Adj. Assoc. Professor (PIL)</li>
      <li>Coach &amp; Supervisor (OKTRAV)</li>
    </ul>
  </section>
</main>
</body>
</html>
```